Looking for a contemporary business card design with our logo

would like to consider a embossing look although I'm not married to the idea. We are a custom jeweler that needs a look that represents old world craftsmanship with a modern twist that's why we went with a more modern shield type of logo that can be stamped inside our rings.
It could be two sided or one we are more after a look the pops and is trendy and creative. (WE ARE NOT LOOKING FOR A COOKIE CUTTER LAYOUT)
We have attached the image and will be using the logo with kestrel forge wording in the format that it's in unless you see a better way of doing it.
If the logo needs a twist we are O.K. with suggestions as well.
This card should scream "Quality" from a high end studio.
Kestrel Forge
4189 Malbrook Rd. Unit C-7
Windsor, CO 80614
www.kestrelforge.example
mo@kestrelforge.example
Should speak quality craftsmanship

```html
<!DOCTYPE html>
<html lang="en">
<head>
<meta charset="utf-8">
<title>Kestrel Forge – Business Card</title>
<link href="https://fonts.googleapis.com/css2?family=Lato:wght@400;700;900&display=swap" rel="stylesheet">
<style>
  :root {
    --backdrop: #e4e4e4;
    --card-light: #fbfbfb;
    --card-dark: #232323;
    --ink: #161616;
    --ink-soft: #3a3a3a;
    --paper-ink: #f5f5f5;
    --rule: #bdbdbd;
  }
  * { box-sizing: border-box; margin: 0; padding: 0; }
  html, body {
    width: 1200px; height: 720px; overflow: hidden;
    background: var(--backdrop);
    font-family: "Lato", Arial, sans-serif;
  }
  .stage { position: relative; width: 1200px; height: 720px; }

  .card {
    position: absolute; top: 241px; width: 420px; height: 237px;
  }
  .card--front { left: 147px; background: var(--card-light); color: var(--ink); }
  .card--back { left: 633px; background: var(--card-dark); color: var(--paper-ink); }

  .brand {
    position: absolute; display: flex; flex-direction: column; align-items: center; gap: 10px;
  }
  .card--front .brand { left: 30px; top: 62px; width: 150px; }
  .card--back .brand { left: 135px; top: 62px; width: 150px; }
  .brand__name {
    font-weight: 700; font-size: 21px; letter-spacing: 0.5px; white-space: nowrap; line-height: 1;
  }
  .brand__mark { width: 62px; height: 62px; background: currentColor; }

  .divider {
    position: absolute; left: 206px; top: 56px; width: 1px; height: 160px; background: var(--rule);
  }
  .contact { position: absolute; left: 223px; top: 55px; }
  .contact__name { font-weight: 900; font-size: 16px; line-height: 1.1; }
  .contact__title { font-size: 10px; margin-top: 3px; color: var(--ink-soft); }
  .contact__address { font-size: 10.5px; line-height: 1.35; margin-top: 22px; color: var(--ink-soft); }
  .contact__list { list-style: none; margin-top: 10px; font-size: 10.5px; color: var(--ink-soft); }
  .contact__list li { display: flex; align-items: center; gap: 6px; line-height: 15px; }
  .contact__list svg { width: 10px; height: 10px; fill: var(--ink); flex: none; }

  .base-band {
    position: absolute; left: 0; bottom: 0; width: 100%; height: 11px;
    border-top: 1.5px solid var(--ink);
    background: linear-gradient(var(--card-light) 0 3px, var(--ink) 3px);
  }
  .card--back .site {
    position: absolute; left: 0; right: 0; top: 215px; text-align: center; font-size: 10.5px;
  }
</style>
</head>
<body>
<main class="stage">
  <section class="card card--front" aria-label="Card front">
    <div class="brand">
      <span class="brand__name">Kestrel Forge</span>
      <span class="brand__mark" aria-hidden="true"></span>
    </div>
    <div class="divider"></div>
    <div class="contact">
      <p class="contact__name">Ray Calder</p>
      <p class="contact__title">President</p>
      <p class="contact__address">4189 Malbrook Rd. Unit C-7<br>Windsor, CO 80614</p>
      <ul class="contact__list">
        <li><svg viewBox="0 0 10 10" aria-hidden="true"><path d="M1 3c0-1.5 1.5-2 4-2s4 .5 4 2v1H7V3H3v1H1z M2 5h6l1 4H1z"/></svg>970-555-0148</li>
        <li><svg viewBox="0 0 10 10" aria-hidden="true"><path d="M0 2h10v6H0z M0.8 2.4 5 5.6l4.2-3.2" stroke="#fbfbfb" stroke-width=".8"/></svg>mo@kestrelforge.example</li>
        <li><svg viewBox="0 0 10 10" aria-hidden="true"><circle cx="5" cy="5" r="4.6"/><path d="M0.5 5h9M5 .5v9M5 .5c-2.2 2.5-2.2 6.5 0 9M5 .5c2.2 2.5 2.2 6.5 0 9" stroke="#fbfbfb" stroke-width=".7" fill="none"/></svg>www.kestrelforge.example</li>
      </ul>
    </div>
    <div class="base-band"></div>
  </section>

  <section class="card card--back" aria-label="Card back">
    <div class="brand">
      <span class="brand__name">Kestrel Forge</span>
      <span class="brand__mark" aria-hidden="true"></span>
    </div>
    <p class="site">www.kestrelforge.example</p>
  </section>
</main>
</body>
</html>
```